Premium stylish simple clever card design for high end construction company.

I need a business card designed that is a standard size and shape (square edges) that is black in colour, with black edges. All text is to be either grey/silver or yellow/gold. On the front I want the logo (supplied as attachment g5) to be embossed or raised to give a texture. I also want the name of my company "The Kestrel Vault (larger font) construction co. (smaller font)" I like the clean style (found in attachment 56419286) of the black background with silver text. But the triangle is to be gold/yellow.

On the back needs to have my contact details. In silver or gold text.

Liam Porter - Builder
Liam@thekestrelvault.com.au
www.thekestrelvault.com.au
0427391065
Lic 517904k
PO BOX 739 Wyndell Bay NSW 2148

Must look simple, elegant and precise.

My work is of the utmost quality and my business card needs to project that. It needs to be simple and precise. It should scream luxury and confidence. Feel free to get creative with the font and font size. If you google "The Kestrel Vault" you will see it has links to great architecture, art, nature and the fibonacci sequence so i am open to using these ideas also.

Target Market(s)

High End home owners. 30-70 year olds.

Industry/Entity Type

Residential Construction

Contact Information for Business Card

Logo and company name on front. Contact details on back.

Font styles to use
Serif
Sans Serif

Colors
ffcf3e

Requirements
Must have
• black background
Nice to have
• debossed logo (silver and gold)
• debased company name (silver)
Should not have
• It should not look like a standard construction business card with pictures of hammers or tools etc.

```html
<!DOCTYPE html>
<html lang="en">
<head>
<meta charset="utf-8">
<title>The Kestrel Vault Construction Co. — Business Card</title>
<link rel="stylesheet" href="https://fonts.googleapis.com/css2?family=Questrial&display=swap">
<style>
  :root {
    --backdrop: #6e6e6e;
    --card: #050505;
    --silver: #b9b9b9;
    --silver-soft: #9a9a9a;
    --rule: #7a7a7a;
    --gold: #b8973a;
    --gold-icon: #9c8236;
  }
  * { box-sizing: border-box; margin: 0; padding: 0; }
  html, body {
    width: 1200px;
    height: 1000px;
    overflow: hidden;
  }
  body {
    position: relative;
    background: var(--backdrop);
    font-family: "Questrial", "Century Gothic", sans-serif;
    color: var(--silver);
  }
  .card {
    position: absolute;
    left: 258px;
    width: 684px;
    height: 400px;
    background: var(--card);
  }
  .card--front { top: 90px; }
  .card--back { top: 533px; }

  /* Front */
  .brand {
    position: absolute;
    inset: 0;
  }
  .brand__dot {
    position: absolute;
    left: 334px;
    top: 160px;
    width: 16px;
    height: 16px;
    border-radius: 50%;
    background: var(--gold);
  }
  .brand__name {
    position: absolute;
    left: 0;
    right: 0;
    top: 237px;
    text-align: center;
    font-size: 38px;
    font-weight: 400;
    line-height: 1;
    letter-spacing: 0.5px;
    color: var(--silver);
    text-transform: uppercase;
  }
  .brand__tagline {
    position: absolute;
    left: 152px;
    width: 374px;
    top: 277px;
    display: flex;
    align-items: center;
    gap: 8px;
    font-size: 16px;
    line-height: 1;
    letter-spacing: 0.6px;
    color: var(--silver-soft);
    text-transform: uppercase;
    white-space: nowrap;
  }
  .brand__tagline::before,
  .brand__tagline::after {
    content: "";
    flex: 1;
    height: 1px;
    background: var(--rule);
  }

  /* Back */
  .holder__name {
    position: absolute;
    right: 28px;
    top: 226px;
    font-size: 26px;
    font-weight: 400;
    line-height: 1;
    letter-spacing: 2.2px;
    color: var(--gold);
    text-transform: uppercase;
  }
  .holder__rule {
    position: absolute;
    left: 24px;
    right: 24px;
    top: 258px;
    height: 1px;
    background: var(--rule);
  }
  .holder__role {
    position: absolute;
    right: 31px;
    top: 263px;
    text-align: right;
    font-size: 17px;
    line-height: 24px;
    color: var(--silver);
  }
  .contact {
    position: absolute;
    left: 29px;
    top: 281px;
    list-style: none;
    font-size: 16px;
    letter-spacing: 0.3px;
    color: var(--silver);
  }
  .contact__item {
    display: flex;
    align-items: center;
    height: 20px;
    gap: 10px;
  }
  .contact__item--address { margin-top: 12px; }
  .contact__icon {
    width: 16px;
    height: 16px;
    flex: none;
    fill: var(--gold-icon);
  }
</style>
</head>
<body>
  <section class="card card--front" aria-label="Card front">
    <div class="brand">
      <span class="brand__dot" aria-hidden="true"></span>
      <h1 class="brand__name">The Kestrel Vault</h1>
      <p class="brand__tagline">Construction Co.</p>
    </div>
  </section>

  <section class="card card--back" aria-label="Card back">
    <h2 class="holder__name">Liam Porter</h2>
    <div class="holder__rule"></div>
    <p class="holder__role">Builder<br>Lic 517904k</p>

    <ul class="contact">
      <li class="contact__item">
        <svg class="contact__icon" viewBox="0 0 16 16" aria-hidden="true"><path d="M1 5c0-2 3-3 7-3s7 1 7 3v1h-4V5H5v1H1z"/><path d="M4 7h8l2 6H2z"/><circle cx="8" cy="10" r="1.6" fill="#050505"/></svg>
        <span>042 7391 065</span>
      </li>
      <li class="contact__item">
        <svg class="contact__icon" viewBox="0 0 16 16" aria-hidden="true"><path d="M1 3h14v10H1z"/><path d="M1.5 3.5 8 9l6.5-5.5" fill="none" stroke="#050505" stroke-width="1.4"/></svg>
        <span>Liam@thekestrelvault.com.au</span>
      </li>
      <li class="contact__item">
        <svg class="contact__icon" viewBox="0 0 16 16" aria-hidden="true"><circle cx="8" cy="8" r="7"/><g fill="none" stroke="#050505" stroke-width="1"><ellipse cx="8" cy="8" rx="3" ry="7"/><path d="M1 8h14M2 4.5h12M2 11.5h12"/></g></svg>
        <span>www.thekestrelvault.com.au</span>
      </li>
      <li class="contact__item contact__item--address">
        <svg class="contact__icon" viewBox="0 0 16 16" aria-hidden="true"><path d="M8 1a5 5 0 0 0-5 5c0 4 5 9 5 9s5-5 5-9a5 5 0 0 0-5-5z"/><circle cx="8" cy="6" r="1.8" fill="#050505"/></svg>
        <span>PO BOX 739 Wyndell Bay NSW 2148</span>
      </li>
    </ul>
  </section>
</body>
</html>
```